Electrical Contractor needs new Flyer

Update: need this flyer asap due to the flyer drop deadline coming soon.
Job Intro:
Design a DL Colour Flyer for a small Electrical Contracting company in the Eastern Suburbs of Melbourne VIC.
Specs:
Size: 99mmx210mm DL.
Paper to be printed on: 150gsm Glossy Paper.
PSD/PDF file must include bleed/crop marks.
Type: Double Sided
Colour: Front and Rear to be FULL colour.
Note: Thanks for the black and white flyers so far, but i think due to the fact iam paying for colour printing anyway, i will go only with colour. (unless you can show me otherwise that black and white can stand out better than colour)
Aim: To Target Local Customers in the area with a flyer that grabs there attention and makes them want to read more, instead of throwing out the flyer.
(there is allready other people putting out flyers in area)
Front Page Includes:
Company name: Peter Calloway Electrical
REC: 48736 (can be small txt in a corner on front side, is legaly required to be displayed)
Phone: 1300 584 272
website: www.pcwiring.com.au
not required but happy to include:
Facebook Logo
www.facebook.com/pcwiring
include visa/mastercard pics
Rear of flyer:
to include work we do etc
We do not have a logo yet for our company, please feel free to design something to suite (keep in mind copyright etc)
you may read our website for info on what we do, but please dont use pictures of jobs etc from our work page. and try not just copy paste text into the flyer. (i can do that myself thats why im getting a designer to add the wow factor to it.
Looking for a Fresh modern looking flyer that will really get the readers attention.
(please no cheap looking cartons pics, also would like australian based looking cables, products if you are using pictures)
any more info please ask me thanks
I have included pics for ref, (such as my current cards and ute signage) please use as examples but dont just base the design on those thanks.
Also inc was my old flyers, i made them ,but they dont fit into the new DL flyer size so need to be re-sized etc.
Note: we may edit or change the winning design in future and this flyer will be copyright to us.

```html
<!DOCTYPE html>
<html lang="en">
<head>
<meta charset="utf-8">
<title>Peter Calloway Electrical – DL Flyer</title>
<link rel="stylesheet" href="https://fonts.googleapis.com/css2?family=Arimo:wght@400;700&family=Cabin:wght@400;500&family=Roboto+Condensed:wght@300;400;700&display=swap">
<style>
  :root {
    --stage: #2b2b2b;
    --navy: #284a80;
    --navy-deep: #1f3c6c;
    --sky: #3f9fd8;
    --sky-light: #8fd6f2;
    --cyan-bubble: #7fcfee;
    --promise-yellow: #f4c20d;
    --ink: #111111;
    --white: #ffffff;
    --muted: #9aa8c2;
    --gold: #d6a92a;
  }
  * { box-sizing: border-box; margin: 0; padding: 0; }
  html, body { width: 1200px; height: 1000px; overflow: hidden; }
  body { background: var(--stage); position: relative; font-family: "Arimo", Arial, sans-serif; }

  .flyer { position: absolute; top: 73px; width: 380px; height: 810px; overflow: hidden; }
  .flyer--rear { left: 142px; background: var(--white); }
  .flyer--front { left: 640px; background: linear-gradient(160deg, #1d5fa8 0%, #2f8fd0 35%, #5bc0ea 55%, #2c6fb4 80%, #27508f 100%); }

  /* Rear */
  .rear-intro { height: 250px; background: var(--navy); color: var(--white); padding: 12px 20px 0 30px; }
  .rec { text-align: right; font-weight: 700; font-size: 12px; letter-spacing: .2px; }
  .rear-intro__title { font-family: "Cabin", sans-serif; font-weight: 400; font-size: 24px; margin-top: 10px; line-height: 1; }
  .rear-intro__text { font-size: 12.6px; line-height: 1.25; margin-top: 4px; }
  .rear-intro__text + .rear-intro__text { margin-top: 17px; }

  .promise { position: relative; height: 350px; padding-top: 6px; }
  .promise__art { position: absolute; left: 150px; top: 40px; width: 120px; height: 260px; border-radius: 60px 60px 20px 20px; background: linear-gradient(180deg, rgba(200,215,230,.35), rgba(200,215,230,.15)); }
  .promise__tab { position: relative; display: inline-block; background: var(--promise-yellow); color: var(--navy-deep); font-weight: 700; font-size: 16px; padding: 4px 46px 5px 30px; clip-path: polygon(0 0, 100% 0, 88% 100%, 0 100%); }
  .promise__list { position: relative; list-style: none; margin: 16px 16px 0 10px; }
  .promise__list li { position: relative; padding-left: 20px; font-size: 12.6px; line-height: 1.3; color: var(--ink); margin-bottom: 15px; }
  .promise__list li::before { content: ""; position: absolute; left: 0; top: 3px; width: 10px; height: 10px; border-radius: 50%; background: var(--ink); }
  .promise__badge { position: absolute; right: 16px; bottom: 10px; width: 72px; height: 52px; }

  .rear-contact { height: 210px; background: var(--navy); color: var(--white); text-align: center; padding-top: 14px; }
  .rear-contact__areas { font-family: "Roboto Condensed", sans-serif; font-weight: 300; font-size: 17.5px; line-height: 1.3; }
  .rear-contact__emergency { color: var(--muted); font-weight: 700; font-size: 17px; margin-top: 12px; }
  .rear-contact__phone { font-family: "Roboto Condensed", sans-serif; font-weight: 700; font-size: 27px; margin-top: 8px; }
  .rear-contact__web { font-family: "Roboto Condensed", sans-serif; font-weight: 300; font-size: 21px; margin-top: 6px; letter-spacing: .3px; }

  /* Front */
  .front-art { position: absolute; left: 0; top: 0; width: 100%; height: 100%; background: radial-gradient(ellipse at 70% 55%, rgba(160,230,250,.55), rgba(60,140,210,0) 60%); }
  .front-character { position: absolute; left: 140px; top: 330px; width: 210px; height: 330px; border-radius: 100px 100px 40px 40px; background: linear-gradient(180deg, rgba(90,210,220,.55), rgba(40,80,140,.45)); }
  .front .rec { position: absolute; right: 22px; top: 22px; color: var(--white); font-size: 15px; }
  .front-brand { position: absolute; left: 0; right: 0; top: 70px; text-align: center; color: var(--white); font-family: "Cabin", sans-serif; font-weight: 400; text-transform: uppercase; }
  .front-brand__mark { display: block; width: 40px; height: 40px; margin: 0 auto 12px; border: 2px solid var(--white); border-radius: 50%; }
  .front-brand__name { font-size: 34px; line-height: 1.05; letter-spacing: 1px; }
  .front-brand__trade { font-size: 24px; letter-spacing: 12px; margin-top: 4px; }
  .front-bubble { position: absolute; left: 20px; top: 225px; width: 230px; height: 220px; }
  .front-bubble__text { position: absolute; left: 67px; top: 272px; width: 140px; text-align: center; font-weight: 700; font-size: 11.5px; line-height: 1.2; color: var(--ink); text-transform: uppercase; }
  .front-contact { position: absolute; left: 0; right: 0; bottom: 70px; text-align: center; color: var(--white); }
  .front-contact__phone { font-family: "Arimo", sans-serif; font-weight: 700; font-size: 44px; }
  .front-contact__web { font-family: "Roboto Condensed", sans-serif; font-weight: 300; font-size: 22px; margin-top: 12px; letter-spacing: .3px; }
</style>
</head>
<body>

<section class="flyer flyer--rear" aria-label="Flyer rear">
  <header class="rear-intro">
    <p class="rec">REC: 48736</p>
    <h1 class="rear-intro__title">Peter Calloway Electrical</h1>
    <p class="rear-intro__text">Contractors is a privately Family owned and operated company providing a comprehensive range of domestic and commercial electrical services throughout Victoria.</p>
    <p class="rear-intro__text">We provide a broad range of electrical services including small electrical jobs around the home to larger commercial electrical works. Our business is underpinned by a commitment to customer service, that is, we turn up on time, we provide quality workmanship at a fair and competitive price.</p>
  </header>

  <div class="promise">
    <div class="promise__art" role="img" aria-label="Faint light bulb character watermark"></div>
    <h2 class="promise__tab">Our Promise to you:</h2>
    <ul class="promise__list">
      <li>We arrive on time. (And keep you up to date, with SMS/Email/PH Job Tracking)</li>
      <li>You will always know the cost before we start the job.</li>
      <li>We Clean up after our selves, leaving your home like it was before we arrived.</li>
      <li>We give you 12months Warranty on all parts, or longer if product has own warranty.</li>
      <li>If theres any problem and its our fault, we will fix it at no cost to you.</li>
      <li>We offer Friendly, helpful Service and Advise.</li>
      <li>We dont charge any Call out Fees</li>
    </ul>
    <svg class="promise__badge" viewBox="0 0 72 52" aria-hidden="true">
      <rect x="2" y="30" width="68" height="12" fill="var(--gold)"/>
      <circle cx="36" cy="24" r="22" fill="var(--gold)"/>
      <circle cx="36" cy="24" r="16" fill="var(--navy)"/>
    </svg>
  </div>

  <footer class="rear-contact">
    <p class="rear-contact__areas">Electrician, Electrical Contractor, Electrics,<br>Lilydale, Ringwood, Croydon, Mooroolbark,<br>Healesville, mt evelyn, chirnside park</p>
    <p class="rear-contact__emergency">24 hour 7 day emergency service</p>
    <p class="rear-contact__phone">1300 584 272</p>
    <p class="rear-contact__web">WWW.PCWIRING.COM.AU</p>
  </footer>
</section>

<section class="flyer flyer--front front" aria-label="Flyer front">
  <div class="front-art" role="img" aria-label="Abstract blue light streaks background"></div>
  <div class="front-character" role="img" aria-label="Energy-saving light bulb character"></div>
  <p class="rec">REC: 48736</p>
  <div class="front-brand">
    <span class="front-brand__mark" aria-hidden="true"></span>
    <p class="front-brand__name">Peter Calloway</p>
    <p class="front-brand__trade">Electrical</p>
  </div>
  <svg class="front-bubble" viewBox="0 0 230 220" aria-hidden="true">
    <path d="M115 12 A100 100 0 1 0 190 180 L212 212 L206 160 A100 100 0 0 0 115 12 Z" fill="var(--cyan-bubble)" stroke="#d8eef8" stroke-width="4"/>
  </svg>
  <p class="front-bubble__text">All electricians are all 'A' class electricians who are fully qualified and accredited. We also offer a genuine 24 hour 7 day emergency service.</p>
  <div class="front-contact">
    <p class="front-contact__phone">1300 584 272</p>
    <p class="front-contact__web">WWW.PCWIRING.COM.AU</p>
  </div>
</section>

</body>
</html>
```